business card design for luxurious real estate brand

using the attached logo, i am looking for a 2-sided business card design. the back should be the gold logo on black background. the front needs to include: gold logo, name, phone, email, and website

Industry/Entity Type

real estate

Contact Information for Business Card

logo, name, email, phone, website

Font styles to use
Sans Serif

```html
<!DOCTYPE html>
<html lang="en">
<head>
<meta charset="UTF-8">
<title>Casa Verlaine – Business Card</title>
<link rel="stylesheet" href="https://fonts.googleapis.com/css2?family=Montserrat:wght@400;500;700&display=swap">
<style>
  :root {
    --backdrop: #efe7c0;
    --card: #000000;
    --gold: #d2ad48;
    --gold-light: #f7e27a;
    --gold-dark: #a8781f;
  }
  * { margin: 0; padding: 0; box-sizing: border-box; }
  html, body { width: 1200px; height: 1000px; overflow: hidden; }
  body {
    background: var(--backdrop);
    font-family: "Montserrat", Arial, sans-serif;
    position: relative;
  }
  .card {
    position: absolute;
    left: 265px;
    width: 670px;
    height: 382px;
    background: var(--card);
    overflow: hidden;
  }
  .card--back { top: 109px; }
  .card--front { top: 509px; }
  .card__band {
    position: absolute;
    left: 0; bottom: 0;
    width: 100%; height: 14px;
    background: linear-gradient(90deg, var(--gold-dark), var(--gold-light) 50%, var(--gold-dark));
  }
  .brand-name {
    position: absolute;
    color: var(--gold);
    font-weight: 500;
    text-transform: uppercase;
    white-space: nowrap;
    text-align: center;
  }
  .card--back .brand-name {
    left: 0; width: 100%;
    top: 250px;
    font-size: 40px;
    letter-spacing: 6px;
  }
  .card--front .brand-name {
    left: 20px; width: 290px;
    top: 224px;
    font-size: 22px;
    letter-spacing: 3.5px;
  }
  .divider {
    position: absolute;
    left: 328px; top: 66px;
    width: 2px; height: 242px;
    background: var(--gold);
  }
  .contact {
    position: absolute;
    left: 363px; top: 86px;
    color: var(--gold);
  }
  .contact__name {
    font-size: 27px;
    font-weight: 700;
    line-height: 30px;
    letter-spacing: 0.5px;
  }
  .contact__role {
    font-size: 20px;
    font-weight: 400;
    line-height: 24px;
    letter-spacing: 1px;
  }
  .contact__list {
    list-style: none;
    margin-top: 93px;
  }
  .contact__phone { font-size: 20px; font-weight: 500; line-height: 28px; }
  .contact__line { font-size: 16.5px; font-weight: 400; line-height: 27px; }
</style>
</head>
<body>
  <section class="card card--back" aria-label="Card back">
    <div class="brand-name">Casa Verlaine</div>
    <div class="card__band"></div>
  </section>

  <section class="card card--front" aria-label="Card front">
    <div class="brand-name">Casa Verlaine</div>
    <div class="divider"></div>
    <div class="contact">
      <div class="contact__name">YOUR NAME</div>
      <div class="contact__role">REALTOR</div>
      <ul class="contact__list">
        <li class="contact__phone">(555) 318-2047</li>
        <li class="contact__line">name@casaverlainehomes.com</li>
        <li class="contact__line">www.casaverlainehomes.com</li>
      </ul>
    </div>
    <div class="card__band"></div>
  </section>
</body>
</html>
```